New small country town business wanting to expand online wants a website to do sales, post local ...

Our logo was designed through Pixel Harbor and we loved it. We would like a website designed for us. We want to be able to sell things online, manage the upkeep ourselves, have a separate page that we can advertise local businesses, a page that contains local information and events, local Buy, sell or swap page, promote tourism in our local area, chat with us. We use Ledgerly and Tillbox We also have a local business Tallowind Creek Cruises - see our website for that www.tallowindcreekcruises.com.au which we promote through our shop 'The Reel Hut'. The Reel Hut sells, hot pies, fishing tackle, bait, groceries, boating accessories, souvenir T-Shirts (also designed by Pixel Harbor) etc. Do you set it up? Do I need to get the hosting done? I dont understand what coding the website means. I apologise for my ignorance. We sell coffee and newspapers to the locals. Provide a meeting place in a town where the only other shop here actively discourages and often verbally abuses the locals.Maree
I apologise for the delay, my father is in hospital and is gravely ill. I have had to fly to Perth to be with him . Can I please have a 2 week extension? Thank you. Mar ee

```html
<!DOCTYPE html>
<html lang="en">
<head>
<meta charset="utf-8">
<title>The Reel Hut</title>
<link href="https://fonts.googleapis.com/css2?family=Lato:wght@400;700;900&display=swap" rel="stylesheet">
<style>
:root{
  --navy:#2a2670;
  --red:#b5121b;
  --red-dark:#9a0d15;
  --text:#333;
  --muted:#555;
  --grey:#f2f2f2;
  --footer:#2b2b2b;
  --footer-base:#1f1f1f;
  --white:#fff;
}
*{box-sizing:border-box;margin:0;padding:0}
html,body{width:1200px;height:3571px;overflow:hidden}
body{font-family:'Lato',sans-serif;color:var(--text);background:var(--white);position:relative}
.abs{position:absolute}
.btn{position:absolute;background:linear-gradient(var(--red),var(--red-dark));color:var(--white);font-weight:700;font-size:17px;text-transform:uppercase;display:flex;align-items:center;justify-content:center;border-radius:2px}
.section-title{position:absolute;left:0;width:1200px;text-align:center;color:var(--navy);font-weight:700;font-size:28px;text-transform:uppercase}

/* header */
.site-header{position:absolute;top:0;left:0;width:1200px;height:114px;background:var(--white);z-index:3}
.logo-oval{position:absolute;left:70px;top:-30px;width:200px;height:162px;border-radius:50%;background:var(--white)}
.logo{position:absolute;left:86px;top:50px;display:flex;align-items:center;gap:10px;color:var(--navy);font-weight:700;font-size:26px}
.logo-dot{width:20px;height:20px;border-radius:50%;background:var(--red)}
.nav a{position:absolute;top:48px;font-size:14px;font-weight:700;color:#333;text-decoration:none;transform:translateX(-50%);text-transform:uppercase}
.nav a.active{color:var(--red)}
.cart-icon{position:absolute;left:1019px;top:36px;width:42px;height:42px;border-radius:50%;background:var(--navy)}
.cart-label{position:absolute;left:1070px;top:48px;font-size:14px;font-weight:700;color:var(--navy)}
.cart-label span{color:var(--red)}

/* hero */
.hero{position:absolute;top:114px;left:0;width:1200px;height:575px;background:linear-gradient(135deg,#2c3b55 0%,#3d5a7a 35%,#1e3450 60%,#15253a 100%)}
.hero-title{position:absolute;top:176px;width:1200px;text-align:center;color:var(--white);font-weight:900;font-size:66px;text-transform:uppercase}
.hero-sub{position:absolute;top:260px;width:1200px;text-align:center;color:var(--white);font-weight:700;font-size:29px;line-height:35px}
.dots{position:absolute;top:525px;left:551px;display:flex;gap:8px}
.dots i{width:28px;height:6px;background:var(--white);border-radius:3px;display:block}
.dots i.on{background:var(--red)}

/* welcome */
.welcome-text{position:absolute;top:800px;left:164px;width:872px;text-align:center;font-size:17px;line-height:34px;color:var(--text)}

/* products */
.band-grey{position:absolute;left:0;width:1200px;background:var(--grey)}
.product{position:absolute;top:1161px;width:242px;height:226px}
.product .ph{width:100%;height:100%}
.product .label{position:absolute;left:0;bottom:0;width:100%;height:53px;background:rgba(30,30,30,.85);color:var(--white);font-weight:700;font-size:17px;display:flex;align-items:center;justify-content:center;text-transform:uppercase}

/* coffee */
.coffee-text{position:absolute;left:614px;top:1661px;width:520px;font-size:17px;line-height:34px;color:var(--text)}

/* tourism */
.tour-card{position:absolute;width:512px;height:178px;background:var(--white);box-shadow:0 1px 5px rgba(0,0,0,.18)}
.tour-card .ph{position:absolute;left:18px;top:18px;width:229px;height:144px}
.tour-card h3{position:absolute;left:273px;top:22px;font-size:17px;color:var(--navy);font-weight:700}
.tour-card p{position:absolute;left:273px;top:56px;font-size:14px;line-height:23px;color:var(--text)}
.tour-card .map{position:absolute;left:273px;top:132px;font-size:14px;font-weight:700;color:var(--red);display:flex;align-items:center;gap:7px}

/* events */
.event{position:absolute;top:2731px;width:331px}
.event .ph{width:100%;height:190px}
.event h3{margin-top:22px;font-size:17px;color:var(--navy);font-weight:700;text-transform:uppercase}
.event p{margin-top:4px;font-size:14px;line-height:24px;color:var(--muted)}
.event p b{color:var(--red)}

/* signup */
.signup{position:absolute;top:3118px;left:0;width:1200px;height:105px;background:var(--navy)}
.signup-label{position:absolute;left:283px;top:42px;color:var(--white);font-weight:700;font-size:17px}
.signup-input{position:absolute;left:427px;top:33px;width:393px;height:40px;background:var(--white);font-size:13px;color:#666;padding:13px 12px}
.signup-btn{position:absolute;left:830px;top:33px;width:89px;height:40px;background:var(--red);color:var(--white);font-weight:700;font-size:14px;display:flex;align-items:center;justify-content:center}

/* footer */
.footer{position:absolute;top:3223px;left:0;width:1200px;height:286px;background:var(--footer);color:#ddd}
.footer-logo{position:absolute;left:75px;top:58px;display:flex;align-items:center;gap:10px;color:var(--white);font-weight:700;font-size:24px}
.footer-logo i{width:18px;height:18px;border-radius:50%;background:var(--white);display:block}
.footer-about{position:absolute;left:75px;top:142px;width:250px;font-size:13px;line-height:25.6px;color:#ccc}
.footer h4{position:absolute;top:37px;font-size:16px;color:var(--white);font-weight:700;text-transform:uppercase}
.sitemap{position:absolute;left:382px;top:72px;font-size:14px;line-height:31.4px;color:#ddd}
.contact{position:absolute;left:575px;top:72px;font-size:13px;line-height:27px;color:#ddd}
.contact .row{display:flex;align-items:center;gap:18px}
.partner{position:absolute;left:852px;display:flex;align-items:center;gap:12px;color:#e8e8e8;font-size:40px;font-weight:400}
.partner i{display:block;width:44px;height:44px;border-radius:50%;border:4px solid #e8e8e8}
.partner i.sq{border-radius:6px}
.live-chat{position:absolute;left:856px;top:215px;width:118px;height:37px;background:var(--white);color:var(--red);font-weight:700;font-size:13px;display:flex;align-items:center;justify-content:center;gap:8px}
.base{position:absolute;top:3509px;left:0;width:1200px;height:62px;background:var(--footer-base)}
.base .copy{position:absolute;left:74px;top:22px;font-size:12px;color:#bbb}
.social{position:absolute;right:80px;top:20px;display:flex;gap:20px}
.social i{display:block;width:20px;height:20px;border-radius:50%;background:#888}
</style>
</head>
<body>

<header class="site-header">
  <div class="logo-oval"></div>
  <div class="logo"><span class="logo-dot"></span>The Reel Hut</div>
  <nav class="nav">
    <a class="active" style="left:475px">Home</a>
    <a style="left:566px">About Us</a>
    <a style="left:673px">Products</a>
    <a style="left:777px">Specials</a>
    <a style="left:862px">Shop</a>
    <a style="left:959px">Contact Us</a>
  </nav>
  <div class="cart-icon">
    <svg width="42" height="42" viewBox="0 0 42 42"><path d="M14 15h3l2 9h8l2-6H18" fill="none" stroke="#fff" stroke-width="2"/><circle cx="20" cy="27" r="1.5" fill="#fff"/><circle cx="26" cy="27" r="1.5" fill="#fff"/></svg>
  </div>
  <div class="cart-label">CART <span>(0)</span></div>
</header>

<section class="hero">
  <div class="abs" role="img" aria-label="Riverside restaurant lit at dusk beside a calm river lined with palm trees" style="inset:0"></div>
  <h1 class="hero-title">The Reel Hut</h1>
  <p class="hero-sub">Sed non neque ac tortor ultricies tristique<br>quisque sed dolor eu metus.</p>
  <div class="btn" style="left:510px;top:361px;width:180px;height:50px">Read More</div>
  <div class="dots"><i class="on"></i><i></i><i></i></div>
</section>

<section>
  <h2 class="section-title" style="top:747px">Welcome to The Reel Hut</h2>
  <p class="welcome-text">Lorem ipsum dolor sit amet, consectetur adipiscing elit. Nulla ornare facilisis erat sit amet maximus. In quis aliquam ligula, vitae ultricies erat. Nam vel malesuada libero. Duis eu nibh ut mi congue cursus nec at lacus. Etiam quis est ut purus iaculis finibus. Etiam eu diam orci. Ut quis massa id mi placerat fringilla.</p>
  <div class="btn" style="left:510px;top:940px;width:180px;height:49px">Read More</div>
</section>

<section class="band-grey" style="top:1043px;height:505px"></section>
<h2 class="section-title" style="top:1095px">Products</h2>
<svg class="abs" style="left:42px;top:1260px" width="18" height="26" viewBox="0 0 18 26"><path d="M14 3L5 13l9 10" fill="none" stroke="#444" stroke-width="4"/></svg>
<svg class="abs" style="left:1140px;top:1260px" width="18" height="26" viewBox="0 0 18 26"><path d="M4 3l9 10-9 10" fill="none" stroke="#444" stroke-width="4"/></svg>
<div class="product" style="left:75px"><div class="ph" role="img" aria-label="Golden baked hot pies" style="background:linear-gradient(135deg,#c89a5e,#8a5a2c)"></div><div class="label">Hot Pies</div></div>
<div class="product" style="left:342px"><div class="ph" role="img" aria-label="Fishing reel with pink line" style="background:linear-gradient(135deg,#b9a38a,#6e5a48)"></div><div class="label">Fishing Tackle</div></div>
<div class="product" style="left:614px"><div class="ph" role="img" aria-label="Hand picking lures from a tackle box" style="background:linear-gradient(135deg,#4f8aa8,#2b5a72)"></div><div class="label">Bait</div></div>
<div class="product" style="left:884px"><div class="ph" role="img" aria-label="Souvenir t-shirts hanging on a shop rack" style="background:linear-gradient(135deg,#e6e6e6,#9a9a9a)"></div><div class="label">Souvenir T-Shirts</div></div>
<div class="btn" style="left:496px;top:1441px;width:208px;height:50px">View All Products</div>

<section>
  <div class="abs" role="img" aria-label="Man reading a newspaper with a coffee" style="left:75px;top:1606px;width:513px;height:320px;background:linear-gradient(135deg,#d8d2c8,#9c8f7e)"></div>
  <h2 class="abs" style="left:614px;top:1616px;font-size:28px;color:var(--navy);font-weight:700">COFFEE &amp; NEWSPAPERS</h2>
  <p class="coffee-text">Lorem ipsum dolor sit amet, consectetur adipiscing elit. Nulla ornare facilisis erat sit amet maximus. In quis aliquam ligula, vitae ultricies erat. Nam vel malesuada libero. Duis eu nibh ut mi congue cursus nec at lacus. Etiam quis est ut purus iaculis finibus. Etiam eu diam orcimassa id mi placerat fringilla.</p>
  <div class="btn" style="left:614px;top:1855px;width:180px;height:50px">Read More</div>
</section>

<section class="band-grey" style="top:1990px;height:625px"></section>
<h2 class="section-title" style="top:2030px">Tourism of Local Area</h2>

<div class="tour-card" style="left:78px;top:2092px">
  <div class="ph" role="img" aria-label="Boats moored at a jetty on a blue bay" style="background:linear-gradient(135deg,#3b7fc4,#7aa9c9)"></div>
  <h3>HEADING TITLE</h3>
  <p>10432 - 123 Street NW<br>Nullam sit amet sapien<br>sollicitudin</p>
  <div class="map"><svg width="10" height="14" viewBox="0 0 10 14"><path d="M5 0a5 5 0 0 1 5 5c0 4-5 9-5 9S0 9 0 5a5 5 0 0 1 5-5z" fill="#b5121b"/><circle cx="5" cy="5" r="2" fill="#fff"/></svg>Map Location</div>
</div>
<div class="tour-card" style="left:614px;top:2092px">
  <div class="ph" role="img" aria-label="Aerial view of a turquoise marina" style="background:linear-gradient(135deg,#1f8fb0,#3fc1c9)"></div>
  <h3>HEADING TITLE</h3>
  <p>10432 - 123 Street NW<br>Nullam sit amet sapien<br>sollicitudin</p>
  <div class="map"><svg width="10" height="14" viewBox="0 0 10 14"><path d="M5 0a5 5 0 0 1 5 5c0 4-5 9-5 9S0 9 0 5a5 5 0 0 1 5-5z" fill="#b5121b"/><circle cx="5" cy="5" r="2" fill="#fff"/></svg>Map Location</div>
</div>
<div class="tour-card" style="left:78px;top:2289px">
  <div class="ph" role="img" aria-label="Canal with a cottage and a moored boat" style="background:linear-gradient(135deg,#6c8fb0,#4a5a3a)"></div>
  <h3>HEADING TITLE</h3>
  <p>10432 - 123 Street NW<br>Nullam sit amet sapien<br>sollicitudin</p>
  <div class="map"><svg width="10" height="14" viewBox="0 0 10 14"><path d="M5 0a5 5 0 0 1 5 5c0 4-5 9-5 9S0 9 0 5a5 5 0 0 1 5-5z" fill="#b5121b"/><circle cx="5" cy="5" r="2" fill="#fff"/></svg>Map Location</div>
</div>
<div class="tour-card" style="left:614px;top:2289px">
  <div class="ph" role="img" aria-label="White motorboat cruising on the water" style="background:linear-gradient(135deg,#9fb8cc,#4f7ea3)"></div>
  <h3>HEADING TITLE</h3>
  <p>10432 - 123 Street NW<br>Nullam sit amet sapien<br>sollicitudin</p>
  <div class="map"><svg width="10" height="14" viewBox="0 0 10 14"><path d="M5 0a5 5 0 0 1 5 5c0 4-5 9-5 9S0 9 0 5a5 5 0 0 1 5-5z" fill="#b5121b"/><circle cx="5" cy="5" r="2" fill="#fff"/></svg>Map Location</div>
</div>
<div class="btn" style="left:510px;top:2505px;width:180px;height:49px">View All Areas</div>

<h2 class="section-title" style="top:2662px">Events</h2>
<div class="event" style="left:75px">
  <div class="ph" role="img" aria-label="Fishing rod and reel off the back of a boat at sea" style="background:linear-gradient(135deg,#5a86c0,#23457a)"></div>
  <h3>Lorem ipsum dolor sit</h3>
  <p>Ametonsectetur adipiscing elit ornare facilisis erat sit amet &nbsp;maximus &nbsp;congue cursus nec at lacus elit non arcu..<b>[+]</b></p>
</div>
<div class="event" style="left:435px">
  <div class="ph" role="img" aria-label="Sailing boats moored along a harbour pier" style="background:linear-gradient(135deg,#4d8fd0,#2c6a8c)"></div>
  <h3>Lorem ipsum dolor sit</h3>
  <p>Ametonsectetur adipiscing elit ornare facilisis erat sit amet &nbsp;maximus &nbsp;congue cursus nec at lacus elit non arcu..<b>[+]</b></p>
</div>
<div class="event" style="left:795px">
  <div class="ph" role="img" aria-label="Friends dining at a table by a marina" style="background:linear-gradient(135deg,#c2c7cf,#6d5b4c)"></div>
  <h3>Lorem ipsum dolor sit</h3>
  <p>Ametonsectetur adipiscing elit ornare facilisis erat sit amet &nbsp;maximus &nbsp;congue cursus nec at lacus elit non arcu..<b>[+]</b></p>
</div>

<section class="signup">
  <div class="signup-label">EMAIL SIGN UP</div>
  <div class="signup-input">Enter Email Address</div>
  <div class="signup-btn">SIGN UP</div>
</section>

<footer class="footer">
  <div class="footer-logo"><i></i>The Reel Hut</div>
  <p class="footer-about">Lorem ipsum dolor sit amet, consec etur adipiscing elitnam tincidunt orci nec orci luctus, quis tincidunt massa molestie.</p>
  <h4 style="left:382px">Site Map</h4>
  <div class="sitemap">Home<br>About Us<br>Products<br>Specials<br>Shop<br>Contact Us</div>
  <h4 style="left:575px">Contact Info</h4>
  <div class="contact">
    218 Tallowind Creek Road<br>
    Marlow Bend, New South Wales 2779
    <div class="row"><svg width="14" height="14" viewBox="0 0 14 14"><path d="M3 1l3 3-2 2c1 2 2 3 4 4l2-2 3 3-2 2C6 13 1 8 1 3z" fill="#ddd"/></svg>+61 2 4390 5527</div>
    <div class="row"><svg width="14" height="12" viewBox="0 0 14 12"><rect x="0" y="1" width="14" height="10" fill="#ddd"/><path d="M0 1l7 5 7-5" fill="none" stroke="#2b2b2b" stroke-width="1.4"/></svg>info@reelhut.com.au</div>
  </div>
  <div class="partner" style="top:38px"><i></i>Ledgerly</div>
  <div class="partner" style="top:116px"><i class="sq"></i>Tillbox</div>
  <div class="live-chat"><svg width="14" height="12" viewBox="0 0 14 12"><ellipse cx="6" cy="5" rx="6" ry="4.5" fill="#b5121b"/><path d="M2 8l-1 3 4-2z" fill="#b5121b"/></svg>LIVE CHAT</div>
</footer>
<div class="base">
  <div class="copy">Copyright © 2019 Company Name. &nbsp;All Rights Reserved.</div>
  <div class="social" aria-label="Social links"><i></i><i></i><i></i><i></i></div>
</div>

</body>
</html>
```